RW Personal Name/Business Card.

I need a double-sided name card with a logo/full design incorporating the "themes/concepts" of:
Neurology, wellness, Animals, Healing, Chiropractic, lifestyle, energy, creatvity & color on both sides of the card.
Information to include:
Name: Rosalind Webb
Mobile #: 0472 816 293
Email spinerwb@mailbrook.net

Possible use of "RW Health & Chiropractic"

Target Market(s)

People of all ages looking to improve their health & lifestyle.

Industry/Entity Type

Business

```html
<!DOCTYPE html>
<html lang="en">
<head>
<meta charset="utf-8">
<title>RW Health &amp; Chiropractic – Business Card Options</title>
<link rel="stylesheet" href="https://fonts.googleapis.com/css2?family=Arimo&family=Lobster&family=Lobster+Two:wght@700&family=Questrial&family=Yellowtail&display=swap">
<style>
  :root {
    --sheet-bg: #000000;
    --card-white: #ffffff;
    --pink: #ff99c8;
    --green: #99cc33;
    --blue: #00ccff;
    --grey: #b2b2b2;
    --ink-light: #ffffff;
  }
  * { box-sizing: border-box; margin: 0; padding: 0; }
  html, body {
    width: 1200px; height: 957px; overflow: hidden;
    background: var(--sheet-bg);
  }
  .sheet { position: relative; width: 1200px; height: 957px; }

  .card {
    position: absolute;
    width: 267px; height: 432px;
    overflow: hidden;
  }
  .card--front { background: var(--accent); }
  .card--back { background: var(--card-white); }

  .theme-pink { --accent: var(--pink); }
  .theme-green { --accent: var(--green); }
  .theme-blue { --accent: var(--blue); }
  .theme-grey { --accent: var(--grey); }

  .name {
    position: absolute;
    right: 13px; bottom: 136px;
    max-width: 240px;
    color: var(--ink-light);
    text-align: right;
    font-weight: 400;
    line-height: 1;
    white-space: nowrap;
  }
  .name--flowing { font-family: "Yellowtail", "Lobster", cursive; font-size: 42px; }
  .name--bold { font-family: "Lobster", cursive; font-size: 38px; }
  .name--caps {
    font-family: "Questrial", "Arimo", sans-serif; font-size: 33px;
    letter-spacing: 1px; line-height: 1.08;
    bottom: 138px;
  }
  .name--stacked { font-family: "Lobster Two", "Lobster", cursive; font-weight: 700; font-size: 43px; line-height: 1; bottom: 140px; }

  .rule {
    position: absolute;
    left: 34px; right: 13px; top: 305px;
    height: 2px; background: var(--ink-light);
  }
  .practice {
    position: absolute;
    right: 13px; top: 314px;
    font-family: "Arimo", Arial, sans-serif;
    font-size: 17px; color: var(--ink-light);
    white-space: nowrap;
  }

  .contact-list { position: absolute; left: 34px; top: 31px; list-style: none; }
  .contact-item {
    display: flex; align-items: center;
    height: 24px; margin-bottom: 6px;
    font-family: "Arimo", Arial, sans-serif;
    font-size: 16px; color: var(--accent);
    white-space: nowrap;
  }
  .contact-icon {
    width: 24px; height: 24px; margin-right: 9px;
    flex: none;
  }
</style>
</head>
<body>
<main class="sheet">

  <!-- Pink option -->
  <section class="card card--front theme-pink" style="left:26px; top:29px;">
    <h1 class="name name--flowing">Rosalind webb</h1>
    <div class="rule"></div>
    <p class="practice">RW Health &amp; chiropractic</p>
  </section>
  <section class="card card--back theme-pink" style="left:306px; top:29px;">
    <ul class="contact-list">
      <li class="contact-item">
        <svg class="contact-icon" viewBox="0 0 24 24" aria-hidden="true"><rect width="24" height="24" rx="4" fill="var(--accent)"/><path d="M5 9c0-2 3-3 7-3s7 1 7 3v1h-3V8.5c-1-.6-2.5-.8-4-.8s-3 .2-4 .8V10H5z M8 11h8l2 7H6z" fill="#fff"/><circle cx="12" cy="14.5" r="1.8" fill="var(--accent)"/></svg>
        0472 816 293
      </li>
      <li class="contact-item">
        <svg class="contact-icon" viewBox="0 0 24 24" aria-hidden="true"><rect width="24" height="24" rx="4" fill="var(--accent)"/><rect x="5" y="7" width="14" height="10" fill="#fff"/><path d="M5 7l7 6 7-6" fill="none" stroke="var(--accent)" stroke-width="1.2"/></svg>
        spinerwb@mailbrook.net
      </li>
    </ul>
  </section>

  <!-- Green option -->
  <section class="card card--front theme-green" style="left:622px; top:29px;">
    <h1 class="name name--bold">Rosalind Webb</h1>
    <div class="rule"></div>
    <p class="practice">RW Health &amp; chiropractic</p>
  </section>
  <section class="card card--back theme-green" style="left:901px; top:29px;">
    <ul class="contact-list">
      <li class="contact-item">
        <svg class="contact-icon" viewBox="0 0 24 24" aria-hidden="true"><rect width="24" height="24" rx="4" fill="var(--accent)"/><path d="M5 9c0-2 3-3 7-3s7 1 7 3v1h-3V8.5c-1-.6-2.5-.8-4-.8s-3 .2-4 .8V10H5z M8 11h8l2 7H6z" fill="#fff"/><circle cx="12" cy="14.5" r="1.8" fill="var(--accent)"/></svg>
        0472 816 293
      </li>
      <li class="contact-item">
        <svg class="contact-icon" viewBox="0 0 24 24" aria-hidden="true"><rect width="24" height="24" rx="4" fill="var(--accent)"/><rect x="5" y="7" width="14" height="10" fill="#fff"/><path d="M5 7l7 6 7-6" fill="none" stroke="var(--accent)" stroke-width="1.2"/></svg>
        spinerwb@mailbrook.net
      </li>
    </ul>
  </section>

  <!-- Blue option -->
  <section class="card card--front theme-blue" style="left:26px; top:496px;">
    <h1 class="name name--caps">ROSALIND<br>WEBB</h1>
    <div class="rule"></div>
    <p class="practice">RW Health &amp; chiropractic</p>
  </section>
  <section class="card card--back theme-blue" style="left:306px; top:496px;">
    <ul class="contact-list">
      <li class="contact-item">
        <svg class="contact-icon" viewBox="0 0 24 24" aria-hidden="true"><rect width="24" height="24" rx="4" fill="var(--accent)"/><path d="M5 9c0-2 3-3 7-3s7 1 7 3v1h-3V8.5c-1-.6-2.5-.8-4-.8s-3 .2-4 .8V10H5z M8 11h8l2 7H6z" fill="#fff"/><circle cx="12" cy="14.5" r="1.8" fill="var(--accent)"/></svg>
        0472 816 293
      </li>
      <li class="contact-item">
        <svg class="contact-icon" viewBox="0 0 24 24" aria-hidden="true"><rect width="24" height="24" rx="4" fill="var(--accent)"/><rect x="5" y="7" width="14" height="10" fill="#fff"/><path d="M5 7l7 6 7-6" fill="none" stroke="var(--accent)" stroke-width="1.2"/></svg>
        spinerwb@mailbrook.net
      </li>
    </ul>
  </section>

  <!-- Grey option -->
  <section class="card card--front theme-grey" style="left:622px; top:496px;">
    <h1 class="name name--stacked">Rosalind<br>Webb</h1>
    <div class="rule"></div>
    <p class="practice">RW Health &amp; chiropractic</p>
  </section>
  <section class="card card--back theme-grey" style="left:901px; top:496px;">
    <ul class="contact-list">
      <li class="contact-item">
        <svg class="contact-icon" viewBox="0 0 24 24" aria-hidden="true"><rect width="24" height="24" rx="4" fill="var(--accent)"/><path d="M5 9c0-2 3-3 7-3s7 1 7 3v1h-3V8.5c-1-.6-2.5-.8-4-.8s-3 .2-4 .8V10H5z M8 11h8l2 7H6z" fill="#fff"/><circle cx="12" cy="14.5" r="1.8" fill="var(--accent)"/></svg>
        0472 816 293
      </li>
      <li class="contact-item">
        <svg class="contact-icon" viewBox="0 0 24 24" aria-hidden="true"><rect width="24" height="24" rx="4" fill="var(--accent)"/><rect x="5" y="7" width="14" height="10" fill="#fff"/><path d="M5 7l7 6 7-6" fill="none" stroke="var(--accent)" stroke-width="1.2"/></svg>
        spinerwb@mailbrook.net
      </li>
    </ul>
  </section>

</main>
</body>
</html>
```